Tarvo Computer Repairs Web Banner

We're after a catchy web banner to advertise the computer repairs business on other web sites and affiliate sites. We manage software, hardware repairs, component upgrades, virus and malware removal and provide online backup solutions.
Please incorporate the logo designed by Ravex, and add our phone number, 1300 482 956 to the banner. The banner will link to the website homepage.

```html
<!DOCTYPE html>
<html lang="en">
<head>
<meta charset="utf-8">
<title>Tarvo Computer Repairs – Web Banner</title>
<link rel="stylesheet" href="https://fonts.googleapis.com/css2?family=Arimo:wght@700&family=Oswald:wght@500&display=swap">
<style>
  :root {
    --page-bg: #e6e7e9;
    --banner-top: #ffffff;
    --banner-bottom: #c3d4ea;
    --frame: #111111;
    --service-red: #cc1420;
    --tick-green: #3e9a1e;
    --tick-dark: #1f5e0d;
    --brand-blue: #1f5aa6;
    --pill-light: #4e9a2a;
    --pill-dark: #0f3a08;
    --pill-text: #ffffff;
  }
  * { margin: 0; padding: 0; box-sizing: border-box; }
  html, body {
    width: 1200px; height: 900px; overflow: hidden;
    background: var(--page-bg);
  }
  .banner {
    position: absolute; left: 375px; top: 262px;
    width: 450px; height: 376px;
    border: 1.5px solid var(--frame);
    background: linear-gradient(to bottom, var(--banner-top) 0%, var(--banner-top) 22%, var(--banner-bottom) 100%);
    font-family: "Arimo", Arial, sans-serif;
    color: inherit; text-decoration: none; display: block;
  }
  .brand-mark {
    position: absolute; left: 33px; top: 40px;
    display: flex; align-items: center; gap: 14px;
  }
  .brand-dot {
    width: 62px; height: 62px; border-radius: 50%;
    background: var(--brand-blue); flex: none;
  }
  .brand-name {
    font-weight: 700; font-size: 26px; line-height: 1.1;
    color: var(--brand-blue);
  }
  .services {
    position: absolute; left: 14px; top: 164px;
    list-style: none;
  }
  .services li {
    display: flex; align-items: center; gap: 6px;
    height: 36px;
    font-weight: 700; font-size: 19.5px; letter-spacing: 1.3px;
    color: var(--service-red); white-space: nowrap;
  }
  .tick { width: 22px; height: 20px; flex: none; }
  .call-pill {
    position: absolute; left: 33px; top: 322px;
    width: 240px; height: 40px; border-radius: 20px;
    background: linear-gradient(to bottom, var(--pill-light) 0%, #2c6e17 45%, var(--pill-dark) 100%);
    border: 1.5px solid #0a2605;
    display: flex; align-items: center; justify-content: center; gap: 8px;
    font-family: "Oswald", "Arial Narrow", sans-serif; font-weight: 500;
    font-size: 29px; color: var(--pill-text); letter-spacing: -0.5px;
  }
  .call-pill svg { width: 26px; height: 26px; }
  .corner-brand {
    position: absolute; right: 12px; bottom: 14px;
    width: 84px; text-align: center;
    font-weight: 700; font-size: 13px; line-height: 1.15;
    color: var(--brand-blue);
  }
</style>
</head>
<body>
  <a class="banner" href="#" aria-label="Tarvo Computer Repairs – visit our website">
    <div class="brand-mark">
      <span class="brand-dot"></span>
      <span class="brand-name">Tarvo<br>Computer Repairs</span>
    </div>

    <ul class="services">
      <li><svg class="tick" viewBox="0 0 22 20"><path d="M2 11 L6 8 L9 12 L18 2 L21 4 L9 18 Z" fill="var(--tick-green)" stroke="var(--tick-dark)" stroke-width="1"/></svg>Software and Hardware Repairs</li>
      <li><svg class="tick" viewBox="0 0 22 20"><path d="M2 11 L6 8 L9 12 L18 2 L21 4 L9 18 Z" fill="var(--tick-green)" stroke="var(--tick-dark)" stroke-width="1"/></svg>Component Upgrades</li>
      <li><svg class="tick" viewBox="0 0 22 20"><path d="M2 11 L6 8 L9 12 L18 2 L21 4 L9 18 Z" fill="var(--tick-green)" stroke="var(--tick-dark)" stroke-width="1"/></svg>Virus and Malware Removals</li>
      <li><svg class="tick" viewBox="0 0 22 20"><path d="M2 11 L6 8 L9 12 L18 2 L21 4 L9 18 Z" fill="var(--tick-green)" stroke="var(--tick-dark)" stroke-width="1"/></svg>Online Backup Solutions</li>
    </ul>

    <div class="call-pill">
      <svg viewBox="0 0 24 24" aria-hidden="true">
        <path d="M6.6 3.5 L9 7.8 L7.3 9.6 C8.4 12 10.3 14 12.6 15.2 L14.4 13.4 L18.7 15.8 L17.3 19.6 C11 19.4 4.7 13 4.6 6.5 Z" fill="var(--pill-text)"/>
        <path d="M14 4.5 A6 6 0 0 1 19.5 10 M14 7.5 A3 3 0 0 1 16.5 10" fill="none" stroke="var(--pill-text)" stroke-width="1.6" stroke-linecap="round"/>
      </svg>
      <span class="phone-number">1300 482 956</span>
    </div>

    <div class="corner-brand">Tarvo Computer Repairs</div>
  </a>
</body>
</html>
```